quorvelbank.com

Design proposals for a gold bank site and gold wallet main page. The site will let people (and companies) open accounts and purchase gold for deposit and later make payments with the gold they hold in the bank. The bank will be a e-money licensed venture located in Switzerland. The functionality of the "system" will be very simple and possibly only use icon symbols so it can be multilingual.

The mainstays of the site will be security and trust. Al digital gold is backed 100 % by visible gold in vault audited every day.

Target Market(s)

Asian and American gold buyers and people preferring gold to currency

Industry/Entity Type

Security

Requirements
Must have
• a) Logo
b) Main index page with a new logo and design
c) System (post log in e-wallet) main page showing the last transactions of the client and give client options to transfer funds and make deposits
Nice to have
• sample contact form
sample faq page
terms page design
Should not have
• So much text since it will be aimed at the worldwide market

```html
<!DOCTYPE html>
<html lang="en">
<head>
<meta charset="utf-8">
<title>Quorvel Bank</title>
<link href="https://fonts.googleapis.com/css2?family=Ubuntu:ital,wght@0,400;0,500;0,700;1,400;1,500&family=Noto+Sans:ital,wght@0,400;1,400&display=swap" rel="stylesheet">
<style>
:root{
  --gold:#f29a00;
  --gold-light:#f6b60a;
  --orange-text:#f08a00;
  --ink:#333;
  --muted:#555;
  --line:#d9d9d9;
  --panel:#f3f3f3;
  --dark:#333;
  --callout:rgba(40,40,40,.82);
  --phone:#f5ef16;
}
*{box-sizing:border-box;margin:0;padding:0}
html,body{width:960px;height:1200px;overflow:hidden}
body{position:relative;font-family:"Noto Sans",sans-serif;color:var(--ink);
  background:linear-gradient(#fff 0 904px,#eeeeee 904px)}
.top-band{position:absolute;left:0;top:0;width:960px;height:326px;
  background:linear-gradient(180deg,var(--gold-light),var(--gold))}
.page{position:absolute;left:96px;top:0;width:768px;height:1132px;background:#fff;
  box-shadow:0 0 6px rgba(0,0,0,.25)}
.abs{position:absolute}
.brand{left:8px;top:16px;height:56px;display:flex;align-items:center;gap:8px;
  font-family:"Ubuntu",sans-serif;font-weight:700;font-size:40px;color:var(--gold);letter-spacing:1px}
.brand-mark{width:14px;height:14px;background:var(--gold)}
.util{right:10px;top:16px;font-family:"Ubuntu",sans-serif;font-size:10px;color:#555}
.util span{color:#aaa;margin:0 4px}
.nav{left:8px;top:89px;width:752px;height:45px;border:1px solid #d0d0d0;border-radius:3px;
  background:linear-gradient(#fdfdfd,#ececec);border-bottom:3px solid #aaa;display:flex;align-items:center;padding-left:6px}
.nav a{font-family:"Ubuntu",sans-serif;font-weight:500;font-size:10.5px;color:#333;text-decoration:none;
  padding:0 17px;line-height:28px;border-right:1px solid #d5d5d5}
.nav a:last-of-type{border-right:0}
.search{position:absolute;right:10px;top:11px;width:164px;height:21px;border:1px solid #c8c8c8;border-radius:3px;
  background:#fff;font-style:italic;font-size:9px;color:#888;padding:4px 9px;overflow:hidden}
.search-btn{position:absolute;right:-1px;top:-1px;width:31px;height:21px;background:var(--gold);border-radius:0 3px 3px 0}
.slider{left:6px;top:146px;width:755px;height:328px;border:1px solid #ddd;padding:4px}
.slide-img{width:745px;height:318px;background:linear-gradient(135deg,#f8c56a,#fbd79a 45%,#f3b45a)}
.callout{left:475px;top:161px;width:269px;height:95px;background:var(--callout);border-radius:10px;
  font-family:"Ubuntu",sans-serif;color:#fff;padding:8px 16px;font-size:18px;font-weight:500;line-height:26px}
.callout b{color:var(--phone);font-size:28px;font-weight:500}
.callout .call{font-size:19px}
.dots{left:14px;top:294px;width:87px;height:20px;background:#222;border-radius:10px;display:flex;gap:5px;align-items:center;padding-left:10px}
.dots i{width:10px;height:10px;border-radius:50%;background:#888}
.dots i:first-child{background:#fff}
.feature{top:494px;width:240px;height:104px;border:1px solid var(--line);border-radius:10px;background:var(--panel);padding:12px 0 0 33px}
.feature li{list-style:none;font-size:10px;color:#444;line-height:20px;position:relative}
.feature li::before{content:"";position:absolute;left:-14px;top:7px;width:6px;height:6px;border-radius:50%;background:#f2b26a}
.divider{left:8px;top:625px;width:752px;height:1px;background:#ddd}
h2{font-family:"Ubuntu",sans-serif;font-weight:400;font-size:18px;color:#333}
.faq{left:8px;width:496px;height:105px;padding:11px 9px 0 9px}
.faq.shaded{background:#f9f9f9;border:1px solid #e6e6e6}
.faq h3{font-family:"Ubuntu",sans-serif;font-weight:400;font-size:10.5px;color:var(--orange-text);line-height:14.5px}
.faq p{font-size:8.4px;color:#555;line-height:14.5px;margin-top:2px}
.faq .meta{position:absolute;left:10px;bottom:8px;font-family:"Ubuntu",sans-serif;font-style:italic;font-size:9.5px;color:#333}
.field{left:520px;width:240px;height:25px;border:1px solid #ccc;background:linear-gradient(#fff,#f3f3f3);
  font-family:"Ubuntu",sans-serif;font-size:11px;color:#888;padding:4px 8px}
.submit{left:694px;top:866px;width:66px;height:20px;background:#333;border-radius:2px;color:#fff;font-family:"Ubuntu",sans-serif;font-size:10.5px;text-align:center;line-height:20px}
.testi{left:520px;top:910px;width:239px;height:201px;border:1px solid #ccc;border-radius:3px;background:#f7f7f7;overflow:hidden}
.testi-head{height:36px;background:linear-gradient(#777,#5e5e5e);color:#fff;font-family:"Ubuntu",sans-serif;font-size:18px;padding:7px 12px}
.quote{padding:10px 12px 0 12px;font-family:"Ubuntu",sans-serif;font-style:italic;font-size:9.4px;color:#444;line-height:16px}
.quote .mark{color:var(--gold);font-size:26px;font-weight:700;font-style:normal;vertical-align:-9px;margin-right:3px;line-height:0}
.quote strong{font-weight:500;color:#222;display:block}
.photo{left:157px;top:132px;width:70px;height:60px;border:2px solid #fff;box-shadow:0 0 2px #aaa;background:linear-gradient(#9ab,#dcc)}
.who{right:88px;top:172px;text-align:right;font-family:"Ubuntu",sans-serif;font-size:9.5px;font-style:italic;color:#333;line-height:12px}
.who small{font-style:normal;font-size:8px;color:#666;display:block}
.footer{left:105px;top:1160px;font-family:"Ubuntu",sans-serif;font-size:9px;color:#555}
.footer em{color:var(--gold);font-style:normal;font-weight:500}
.social{left:785px;top:1161px;display:flex;gap:7px}
.social i{width:12px;height:12px;border-radius:2px}
</style>
</head>
<body>
<div class="top-band"></div>
<div class="page">
  <div class="abs brand"><span class="brand-mark"></span>QUORVEL</div>
  <div class="abs util">Support<span>|</span>FAQ<span>|</span>Branches<span>|</span>Member</div>

  <nav class="abs nav">
    <a>HOME</a><a>ABOUT US</a><a>SERVICES</a><a>DEPOSIT</a><a>TESTIMONIALS</a><a>CONTACT US</a>
    <div class="search">Search here..<div class="search-btn">
      <svg width="31" height="21" viewBox="0 0 31 21"><circle cx="14" cy="9" r="4" fill="none" stroke="#222" stroke-width="1.8"/><line x1="17" y1="12" x2="21" y2="15" stroke="#222" stroke-width="2.2"/></svg>
    </div></div>
  </nav>

  <div class="abs slider">
    <div class="slide-img" role="img" aria-label="Hand holding a stack of hundred-dollar bills above rising stacks of gold coins"></div>
    <div class="abs callout">Do You Have Account ?<br>Open NOW !<br><span class="call">Call: </span><b>555 014 2278</b></div>
    <div class="abs dots"><i></i><i></i><i></i><i></i><i></i></div>
  </div>

  <ul class="abs feature" style="left:8px">
    <li>Lorem ipsum dolor sit amet.</li><li>Nam fermentum vestibulum purus id .</li><li>Aliquam ullamcorper tempor felis.</li><li>Morbi iaculis fringilla gravida.</li>
  </ul>
  <ul class="abs feature" style="left:264px">
    <li>Lorem ipsum dolor sit amet.</li><li>Nam fermentum vestibulum purus id .</li><li>Aliquam ullamcorper tempor felis.</li><li>Morbi iaculis fringilla gravida.</li>
  </ul>
  <ul class="abs feature" style="left:520px">
    <li>Lorem ipsum dolor sit amet.</li><li>Nam fermentum vestibulum purus id .</li><li>Aliquam ullamcorper tempor felis.</li><li>Morbi iaculis fringilla gravida.</li>
  </ul>

  <div class="abs divider"></div>

  <h2 class="abs" style="left:9px;top:639px">Frequently Asked Question</h2>
  <div class="abs faq shaded" style="top:674px">
    <h3>Lorem ipsum dolor sit amet, consectetur adipiscing elit. Fusce accumsan, elit a suscipit sagittis, tortor sapien cursus risus, non rhoncus lectus nunc ac nulla?</h3>
    <p>Aliquam molestie, mi et imperdiet euismod, dui purus auctor tellus, et interdum lacus lectus et ante. Sed accum-san sollicitudin sapien, sit amet adipiscing turpis gravida ac. In congue, neque ac lobortis volutpat..</p>
    <div class="meta">Learn More &nbsp;|&nbsp; Author Name</div>
  </div>
  <div class="abs faq" style="top:792px">
    <h3>Nam fermentum vestibulum purus id aliquet. Phasellus dui ante, ultricies et sollicitudin pretium, fermentum vel velit?</h3>
    <p>Vestibulum ante ipsum primis in faucibus orci luctus et ultrices posuere cubilia Curae; Ut et scelerisque ante. Donec erat purus, faucibus vitae congue vel, porttitor nec lectus...</p>
    <div class="meta">Learn More &nbsp;|&nbsp; Author Name</div>
  </div>
  <div class="abs faq shaded" style="top:910px">
    <h3>Aliquam ullamcorper tempor felis, nec condimentum odio aliquet vitae. Morbi iaculis fringilla gravida?</h3>
    <p>Nunc dignissim lectus vitae eros placerat euismod. Aenean lacinia sodales eros, sit amet molestie enim consecte-tur eget. Sed vel magna vel eros adipiscing adipiscing eu sit amet turpis pellentesque...</p>
    <div class="meta">Learn More &nbsp;|&nbsp; Author Name</div>
  </div>
  <div class="abs faq" style="top:1028px;height:100px">
    <h3>Nam fermentum vestibulum purus id aliquet. Phasellus dui ante, ultricies et sollicitudin pretium, fermentum vel velit?</h3>
    <p>Vestibulum ante ipsum primis in faucibus orci luctus et ultrices posuere cubilia Curae; Ut et scelerisque ante. Donec erat purus, faucibus vitae congue vel, porttitor nec lectus...</p>
    <div class="meta">Learn More &nbsp;|&nbsp; Author Name</div>
  </div>

  <h2 class="abs" style="left:520px;top:639px">Contact Us</h2>
  <div class="abs field" style="top:674px">Name</div>
  <div class="abs field" style="top:706px">Email Address</div>
  <div class="abs field" style="top:739px">Contact No.</div>
  <div class="abs field" style="top:771px;height:85px">Message</div>
  <div class="abs submit">Submit</div>

  <div class="abs testi">
    <div class="testi-head">Testimonials</div>
    <div class="quote"><span class="mark">“</span>In congue, neque ac lobortis volutpat, libero mauris varius mi, vitae suscipit ipsum ligula vitae risus. Duis aliquam nibh a dui iaculis viverra id a velit....<strong>Read More</strong></div>
    <svg class="abs" style="left:80px;top:134px" width="58" height="24" viewBox="0 0 58 24"><path d="M3 3 Q20 18 54 18" fill="none" stroke="#f29a00" stroke-width="2"/><path d="M47 13 L54 18 L47 22" fill="none" stroke="#f29a00" stroke-width="2"/></svg>
    <div class="abs who">Daniel Marsh<small>Senior assistant</small></div>
    <div class="abs photo" role="img" aria-label="Portrait photo of the client giving the testimonial"></div>
  </div>
</div>

<div class="abs footer">Copyright © 2012 &nbsp;<em>QUORVEL.</em> All Right Reserved &nbsp;|&nbsp; Privacy Policy</div>
<div class="abs social">
  <i style="background:#3b5a9a"></i><i style="background:#3ea4dc"></i><i style="background:#1c6fa6"></i><i style="background:#f07a1a"></i>
</div>
</body>
</html>
```